Construction Company Cellar Horizon needs Business Card

I would like modern looking business card design. I am attaching logo of our company. Please include cell nr 415.837.6042 , email address cellarhorizon7x@mailbrook.net, web : cellarhorizon7x.net, please also include wording: Specializing in finishing and remodeling basements. You can play with dark grey and orange colors or any ideas are welcome. Also include social media icons Chatterly and NestFinder.

```html
<!DOCTYPE html>
<html lang="en">
<head>
<meta charset="utf-8">
<title>Cellar Horizon – Business Card</title>
<link rel="stylesheet" href="https://fonts.googleapis.com/css2?family=Michroma&family=Open+Sans:wght@400;600&display=swap">
<style>
  :root {
    --canvas: #e9e6e2;
    --card: #121212;
    --card-edge: #1c1c1c;
    --orange: #f05a28;
    --white: #ffffff;
    --grey: #c9c9c9;
    --muted: #8a8a8a;
  }
  * { box-sizing: border-box; margin: 0; padding: 0; }
  html, body { width: 1200px; height: 900px; overflow: hidden; }
  body {
    background: var(--canvas);
    font-family: "Open Sans", Arial, sans-serif;
    display: flex;
    flex-direction: column;
    align-items: center;
    justify-content: center;
    gap: 40px;
  }
  .card {
    width: 700px;
    height: 400px;
    background: radial-gradient(ellipse at 50% 40%, var(--card-edge), var(--card) 70%);
    position: relative;
    overflow: hidden;
    box-shadow: 0 6px 18px rgba(0,0,0,.25);
  }
  .brand-name {
    font-family: "Open Sans", Arial, sans-serif;
    font-weight: 600;
    color: var(--orange);
    text-transform: uppercase;
    letter-spacing: 3px;
    display: flex;
    align-items: center;
    gap: 14px;
  }
  .brand-mark {
    width: 16px; height: 16px;
    background: var(--white);
  }
  /* back side */
  .card-back { display: flex; flex-direction: column; align-items: center; justify-content: center; gap: 46px; }
  .card-back .brand-name { font-size: 40px; }
  .social { display: flex; gap: 34px; }
  .social-item {
    display: flex; align-items: center; gap: 8px;
    color: var(--grey); font-size: 15px;
  }
  .social-dot { width: 12px; height: 12px; border-radius: 50%; background: var(--orange); }
  /* front side */
  .holder { position: absolute; left: 46px; top: 58px; }
  .holder-name {
    font-family: "Michroma", "Open Sans", sans-serif;
    color: var(--orange);
    font-size: 24px;
    letter-spacing: 1px;
  }
  .holder-title { color: var(--grey); font-size: 16px; margin-top: 4px; }
  .card-front .brand-name { position: absolute; right: 40px; top: 130px; font-size: 30px; }
  .contacts { position: absolute; left: 46px; top: 206px; list-style: none; }
  .contacts li {
    display: flex; align-items: center; gap: 10px;
    color: var(--white); font-size: 19px; line-height: 30px;
  }
  .contacts svg { width: 14px; height: 14px; fill: var(--orange); flex: none; }
  .tagline-band {
    position: absolute; left: 0; right: 0; bottom: 0; height: 82px;
    background: var(--orange);
    display: flex; align-items: center; justify-content: center;
    color: var(--white); font-size: 20px; text-transform: uppercase; letter-spacing: .3px;
  }
</style>
</head>
<body>
  <section class="card card-back" aria-label="Card back">
    <div class="brand-name"><span class="brand-mark"></span>Cellar Horizon</div>
    <div class="social">
      <span class="social-item"><span class="social-dot"></span>Chatterly</span>
      <span class="social-item"><span class="social-dot"></span>NestFinder</span>
    </div>
  </section>

  <section class="card card-front" aria-label="Card front">
    <div class="holder">
      <div class="holder-name">MARCUS DELGADO</div>
      <div class="holder-title">Managing Director</div>
    </div>
    <div class="brand-name"><span class="brand-mark"></span>Cellar Horizon</div>
    <ul class="contacts">
      <li>
        <svg viewBox="0 0 14 14" aria-hidden="true"><rect x="3" y="0" width="8" height="14" rx="1.5"/><rect x="4.5" y="2" width="5" height="8" fill="#121212"/></svg>
        415.837.6042
      </li>
      <li>
        <svg viewBox="0 0 14 14" aria-hidden="true"><rect x="0" y="2" width="14" height="10" rx="1"/><path d="M1 3 L7 8 L13 3" stroke="#121212" stroke-width="1.4" fill="none"/></svg>
        cellarhorizon7x@mailbrook.net
      </li>
      <li>
        <svg viewBox="0 0 14 14" aria-hidden="true"><circle cx="7" cy="7" r="7"/><path d="M0 7 H14 M7 0 V14" stroke="#121212" stroke-width="1.2"/><ellipse cx="7" cy="7" rx="3" ry="6.5" fill="none" stroke="#121212" stroke-width="1.2"/></svg>
        cellarhorizon7x.net
      </li>
    </ul>
    <div class="tagline-band">Specializing in finishing and remodeling basements.</div>
  </section>
</body>
</html>
```